Real Estate and Property Management Company needs new listings

We need a business card for our company, Corvell Realty & Property Management. We maximize financial returns on residential investment properties. By evaluating the current value and health of a property, we devise a financial plan to rehabilitate the property while earning an income over a period of years for rental properties, or suggest meaningful updates and improvements to ensure maximum payout on sales properties.
We would like to see our business cards with the colors black and metallic burgundy. The final design should communicate management and financial growth.

Target Market(s)

Home Owners of single family, detatched residential homes.

Industry/Entity Type

Business

Contact Information for Business Card

Side 1: Dana Corvell
Broker, Owner
Dana@CorvellHomesite.example
555-274-8061 (Cell)
555-318-4470 (Office)
Please incorporate in the design of side 1 that we have been in business for 40 years, along with communicating sales and management.
Side 2: Marisa Corvell
Property Manager
Marisa@CorvellHomesite.example
555-274-8095 (Cell)
555-318-4470 (Office)
Please incorporate that we are a family owner and operated company on side 2.

Font styles to use
Serif

Requirements
Must have
• Elegant, feminine design of metallic burgundy on black on double sided card.
Nice to have
• I would like to see some consistency of design on the front and back of the card, with perhaps a bold, thick line of burgundy on the right, vertical side. I would also like the black card stock to have some geometrical design or texture.
Should not have
• Any of the colors provided below. I cannot choose burgundy, which is the color for our business. Is this the only color selection available?

```html
<!DOCTYPE html>
<html lang="en">
<head>
<meta charset="utf-8">
<title>Corvell Realty &amp; Property Management — Business Card</title>
<link href="https://fonts.googleapis.com/css2?family=Cinzel:wght@500;600&family=Open+Sans:wght@400;600&family=Oswald:wght@500;600&family=Playfair+Display:ital,wght@0,400;1,400&display=swap" rel="stylesheet">
<style>
  :root {
    --backdrop: #d9d9d9;
    --card-black: #222222;
    --line-dark: #1a1a1a;
    --burgundy-deep: #5c0008;
    --burgundy: #9c0a14;
    --burgundy-hi: #b3121c;
    --cream: #ede3d6;
    --cream-text: #efe6da;
    --ink: #1c1c1c;
  }
  * { box-sizing: border-box; margin: 0; padding: 0; }
  html, body { width: 1200px; height: 900px; overflow: hidden; }
  body {
    background: linear-gradient(90deg, #e4e4e4, #c9c9c9);
    position: relative;
  }
  .card {
    position: absolute;
    width: 540px;
    height: 310px;
    background: var(--card-black);
    box-shadow: 0 6px 18px rgba(0,0,0,0.18);
    overflow: hidden;
  }
  .card--company { left: 40px; top: 295px; }
  .card--person { left: 620px; top: 295px; }

  .band {
    position: absolute;
    background: linear-gradient(90deg, var(--burgundy-deep), var(--burgundy-hi) 45%, var(--burgundy) 70%, var(--burgundy-deep));
  }
  .band::before, .band::after {
    content: "";
    position: absolute;
    top: 0; bottom: 0;
    width: 5px;
    background: var(--line-dark);
  }
  .band::before { left: 10px; }
  .band::after { right: 10px; }

  /* company side */
  .card--company .band { left: 205px; width: 125px; }
  .band--upper { top: 0; height: 108px; }
  .band--lower { top: 212px; height: 98px; }
  .rule-pair {
    position: absolute;
    left: 205px; width: 125px; height: 9px;
    border-top: 2px solid var(--burgundy);
    border-bottom: 2px solid var(--burgundy);
  }
  .rule-pair--upper { top: 111px; }
  .rule-pair--lower { top: 200px; }
  .company-name {
    position: absolute;
    left: 0; right: 0; top: 124px;
    text-align: center;
    color: var(--cream-text);
    font-family: "Playfair Display", serif;
  }
  .company-name__lead { display: block; font-size: 25px; line-height: 1; letter-spacing: 0.2px; margin-left: -10px; }
  .company-name__amp { display: block; font-style: italic; font-size: 16px; line-height: 1.1; margin-left: -10px; }
  .company-name__tail { display: block; font-size: 15px; line-height: 1.05; margin-left: -10px; }
  .company-tag {
    position: absolute;
    left: 0; right: 0; top: 187px;
    text-align: center;
    margin-left: -10px;
    color: var(--cream-text);
    font-family: "Open Sans", sans-serif;
    font-size: 10px;
    letter-spacing: 3px;
  }

  /* person side */
  .card--person .band { left: 228px; width: 108px; top: 0; height: 310px; }
  .panel {
    position: absolute;
    left: 26px; top: 28px;
    width: 488px; height: 236px;
    background: var(--cream);
  }
  .person-name {
    position: absolute;
    left: 0; right: 0; top: 34px;
    text-align: center;
    font-family: "Cinzel", serif;
    font-weight: 600;
    font-size: 27px;
    color: var(--ink);
    letter-spacing: 0.5px;
  }
  .person-role {
    position: absolute;
    left: 0; right: 0; top: 72px;
    text-align: center;
    font-family: "Open Sans", sans-serif;
    font-size: 13px;
    color: var(--ink);
    letter-spacing: 0.6px;
  }
  .flourish {
    position: absolute;
    left: 150px; top: 98px;
    width: 190px; height: 26px;
    background: linear-gradient(90deg, transparent, rgba(28,28,28,0.18), transparent);
  }
  .contact {
    position: absolute;
    width: 120px;
    text-align: center;
    font-family: "Oswald", sans-serif;
    font-weight: 600;
    color: var(--ink);
  }
  .contact__icon { display: block; margin: 0 auto; height: 24px; }
  .contact__rule { display: block; height: 1px; background: var(--ink); margin: 1px 6px 4px; }
  .contact__text { display: block; font-size: 12px; letter-spacing: 2px; }
  .contact--cell { left: 12px; top: 140px; }
  .contact--office { left: 184px; top: 170px; }
  .contact--email { left: 308px; top: 186px; width: 172px; }
  .contact--email .contact__text { font-size: 10px; letter-spacing: 0; }
  .experience {
    position: absolute;
    right: 24px; bottom: 12px;
    font-family: "Open Sans", sans-serif;
    font-size: 12px;
    color: var(--cream-text);
  }
</style>
</head>
<body>
  <section class="card card--company" aria-label="Company side">
    <div class="band band--upper"></div>
    <div class="rule-pair rule-pair--upper"></div>
    <h1 class="company-name">
      <span class="company-name__lead">Corvell Realty</span>
      <span class="company-name__amp">&amp;</span>
      <span class="company-name__tail">Property Management</span>
    </h1>
    <p class="company-tag">Family Business</p>
    <div class="rule-pair rule-pair--lower"></div>
    <div class="band band--lower"></div>
  </section>

  <section class="card card--person" aria-label="Contact side">
    <div class="band"></div>
    <div class="panel">
      <h2 class="person-name">Dana Corvell</h2>
      <p class="person-role">Broker, Owner</p>
      <div class="flourish" role="img" aria-label="Decorative scroll flourish"></div>

      <div class="contact contact--cell">
        <svg class="contact__icon" viewBox="0 0 24 24" width="24" height="24" aria-hidden="true">
          <rect x="7" y="2" width="10" height="20" rx="2" fill="#1c1c1c"/>
          <rect x="9" y="5" width="6" height="11" fill="#ede3d6"/>
        </svg>
        <span class="contact__rule"></span>
        <span class="contact__text">555-274-8061</span>
      </div>

      <div class="contact contact--office">
        <svg class="contact__icon" viewBox="0 0 24 24" width="24" height="24" aria-hidden="true">
          <path d="M6.6 10.8c1.4 2.8 3.8 5.1 6.6 6.6l2.2-2.2c.3-.3.7-.4 1-.2 1.1.4 2.3.6 3.6.6.6 0 1 .4 1 1V20c0 .6-.4 1-1 1C10.6 21 3 13.4 3 4c0-.6.4-1 1-1h3.5c.6 0 1 .4 1 1 0 1.3.2 2.5.6 3.6.1.3 0 .7-.2 1L6.6 10.8z" fill="#1c1c1c"/>
        </svg>
        <span class="contact__rule"></span>
        <span class="contact__text">555-318-4470</span>
      </div>

      <div class="contact contact--email">
        <svg class="contact__icon" viewBox="0 0 24 24" width="24" height="24" aria-hidden="true">
          <path d="M3 7h18v12H3z" fill="#1c1c1c"/>
          <path d="M3 7l9 7 9-7" fill="none" stroke="#ede3d6" stroke-width="1.4"/>
        </svg>
        <span class="contact__rule"></span>
        <span class="contact__text">Dana@CorvellHomesite.example</span>
      </div>
    </div>
    <p class="experience">40 years of experience...</p>
  </section>
</body>
</html>
```